Webdesign für Raumgestalter / Interior Designer und Implementierung
Zielgruppe
Wir möchten zukünftig für Menschen «Träume in Räume» verwandeln und sind spezialisiert auf Interior Design, ReDesign Home Staging wie auch Dekorationen mit folgenden Leistungen an:
- Interior Design
- Home Styling
- Home Staging
- Dekoration
Aufgabenstellung
(Wichtig: Bitte Anforderungen und Fotos im PDF File im Anhang beachten)
Aufbau der Homepage
Homepage wird in verschiedenen Seiten/Fenster aufgebaut. Diese können oben auf der Homepage angeklickt werden. Der Aufbau ist in 5 Seiten: Home, Leistungen, Referenzen, Pakete und Preise, Kontakt
- Die Homepage sollte dann von uns gemanagt werden können. (Bspw. Plattformen oder andere Gremien, wo die Homepage einfach und ohne tiefe Informatikkenntnisse gemanagt werden kann :-).)
- Die Leistungen betreffen Templating inkl. Umsetzung (Online-Fertigstellung), ich kann bei der URL-Verknüpfung unterstützen.
1) Home
Willkommensseite, inspirierend, einladend, sollte die Besucher dazu animieren vertiefter die Detail anzuschauen.
Es soll ein Button unten ermöglichen, ins zweite Fenster «Referenzen» zu klicken. Siehe unteres Kapitel.
2) Leistungen
a. Interior Design
b. Home Styling
c. Home Staging
d. Dekoration
Hier wird der Ablauf von Projekten aufgezeigt, dieser bildet sich in:
- Planung, Designen, Realisieren
Weiterer sollen realisierte Design-Projekte von bspw. Räumen mit Fotos aufgeführt sein.
3) Referenzen
- Dieses Fenster soll das Interesse möglicher Kunden im Detail erwecken
- Es soll ein erster Termin telefonisch oder per Videocall stattfinden können
(dient zum Kennenlernen, Bedürfnisse verstehen, Ablauf aufzeigen)
4) Pakete und Preise
Hier werden die Pakete und Preise beschrieben.
Die Preise werden auf Rapportsbasis erstellt und richten sich nach Offerten und Wünschen des Kunden. Preis ist bei 80 Franken pro Stunde, das erste Beratungsgespräch wird nicht verrechnet.
Hier können Details in einer Tabelle / Preisliste erarbeitet werden:
- Private Wohnräume
o Private Wohnung
o Privates Haus
o Ferienimmobilien
- Business Einrichtungen
o Einrichtungen von Geschäften
o NestoFlat-Einrichtungen
o ReDesign für Verkauf von Immo..

```html
<!DOCTYPE html>
<html lang="de">
<head>
<meta charset="utf-8">
<title>Raumwerk – Leistungen</title>
<link href="https://fonts.googleapis.com/css2?family=Poppins:wght@500;600&family=Roboto:wght@400&display=swap" rel="stylesheet">
<style>
  :root {
    --header-bg: #404040;
    --footer-bg: #353535;
    --green: #475e50;
    --ink: #222222;
    --white: #ffffff;
    --button-grey: #b5b5b5;
    --line: rgba(255,255,255,0.75);
    --builder-teal: #1f6e7a;
  }
  * { margin: 0; padding: 0; box-sizing: border-box; }
  html, body { width: 969px; height: 1200px; overflow: hidden; background: var(--white); }
  body { position: relative; font-family: 'Roboto', sans-serif; color: var(--ink); }
  .abs { position: absolute; }

  .site-header { left: 0; top: 0; width: 969px; height: 74px; background: var(--header-bg); border-bottom: 1px solid #2c2c2c; }
  .brand { left: 23px; top: 15px; width: 72px; height: 44px; background: var(--white); display: flex; align-items: center; justify-content: center; font-family: 'Poppins', sans-serif; font-weight: 500; font-size: 10px; color: var(--ink); letter-spacing: 0.5px; }
  .main-nav { left: 0; top: 30px; width: 969px; display: flex; justify-content: center; gap: 23px; padding-right: 10px; }
  .main-nav a { color: var(--white); font-size: 9.5px; text-decoration: none; padding-bottom: 3px; }
  .main-nav a.active { border-bottom: 1.5px solid var(--white); }
  .header-cta { left: 871px; top: 26px; width: 68px; height: 22px; background: var(--button-grey); border-radius: 3px; color: var(--white); font-size: 9.5px; display: flex; align-items: center; justify-content: center; }

  .page-title { left: 104px; top: 117px; font-family: 'Poppins', sans-serif; font-weight: 600; font-size: 29px; color: var(--ink); }
  .service { top: 180px; width: 177px; }
  .service-photo { width: 177px; height: 177px; }
  .service h2 { font-family: 'Poppins', sans-serif; font-weight: 600; font-size: 14.5px; margin-top: 11px; }
  .service p { font-size: 10.5px; margin-top: 12px; }

  .process { left: 0; top: 488px; width: 969px; height: 251px; background: var(--green); color: var(--white); }
  .process-title { left: 104px; top: 46px; font-family: 'Poppins', sans-serif; font-weight: 600; font-size: 28px; line-height: 36px; }
  .step { left: 375px; width: 490px; height: 65px; font-family: 'Poppins', sans-serif; font-weight: 600; font-size: 14.5px; display: flex; justify-content: space-between; align-items: center; }
  .step.rule { border-bottom: 1px solid var(--line); }

  .projects { left: 0; top: 739px; width: 969px; height: 231px; background: linear-gradient(90deg, #f7f5f1 0%, #f1eee8 45%, #e7e5e1 70%, #dcd8d2 100%); }
  .projects-veil { left: 0; top: 0; width: 969px; height: 231px; background: radial-gradient(ellipse at 45% 50%, rgba(255,255,255,0.7), rgba(255,255,255,0) 70%); }
  .projects h2 { left: 0; top: 60px; width: 969px; text-align: center; font-family: 'Poppins', sans-serif; font-weight: 600; font-size: 21px; }
  .projects p { left: 0; top: 100px; width: 969px; text-align: center; font-size: 10.5px; }
  .projects-button { left: 443px; top: 137px; width: 82px; height: 29px; background: #000; color: var(--white); border-radius: 3px; font-size: 9.5px; display: flex; align-items: center; justify-content: center; }

  .site-footer { left: 0; top: 970px; width: 969px; height: 150px; background: var(--footer-bg); color: var(--white); font-size: 9.5px; }
  .footer-contact { left: 0; top: 48px; width: 969px; text-align: center; }
  .footer-links { left: 0; top: 100px; width: 969px; display: flex; justify-content: center; gap: 12px; }
  .site-footer a { color: var(--white); text-decoration: underline; }

  .builder-note { left: 0; top: 1155px; width: 969px; display: flex; justify-content: center; align-items: center; gap: 6px; font-size: 8px; color: var(--ink); }
  .builder-name { font-family: 'Poppins', sans-serif; font-weight: 600; font-size: 11px; color: var(--builder-teal); }
  .builder-note a { color: var(--ink); }
</style>
</head>
<body>
  <header class="site-header abs">
    <div class="brand abs">Raumwerk</div>
    <nav class="main-nav abs">
      <a href="#">Home</a>
      <a href="#" class="active">Leistungen</a>
      <a href="#">Referenzen</a>
      <a href="#">Pakete und Preise</a>
      <a href="#">Kontakt</a>
    </nav>
    <div class="header-cta abs">Kontakt</div>
  </header>

  <h1 class="page-title abs">Meine Leistungen</h1>

  <article class="service abs" style="left:104px">
    <div class="service-photo" role="img" aria-label="Foto eines Schlafzimmers mit violetten Vorhängen" style="background:linear-gradient(135deg,#8a6f93 0%,#6a4f78 45%,#d8d0d6 100%)"></div>
    <h2>Interior Design</h2>
    <p>Fliesstext / Begriffserklärung</p>
  </article>
  <article class="service abs" style="left:298px">
    <div class="service-photo" role="img" aria-label="Foto eines Bücherregals aus Holz" style="background:linear-gradient(180deg,#3a2c22 0%,#8a6a45 50%,#4a3424 100%)"></div>
    <h2>Home Styling</h2>
    <p>Fliesstext / Begriffserklärung</p>
  </article>
  <article class="service abs" style="left:493px">
    <div class="service-photo" role="img" aria-label="Foto eines hellen Essbereichs mit Parkettboden" style="background:linear-gradient(180deg,#f1f1f0 0%,#e4e2df 60%,#b79c7c 100%)"></div>
    <h2>Home Staging</h2>
    <p>Fliesstext / Begriffserklärung</p>
  </article>
  <article class="service abs" style="left:687px">
    <div class="service-photo" role="img" aria-label="Foto von Pendelleuchten aus Bernsteinglas" style="background:linear-gradient(135deg,#2e2a24 0%,#8a6a3a 50%,#3c3a34 100%)"></div>
    <h2>Dekoration</h2>
    <p>Fliesstext / Begriffserklärung</p>
  </article>

  <section class="process abs">
    <h2 class="process-title abs">Schritt<br>für<br>Schritt</h2>
    <div class="step rule abs" style="top:29px"><span>Planung</span>
      <svg width="16" height="16" viewBox="0 0 16 16"><path d="M8 1v14M1 8h14" stroke="#fff" stroke-width="1.3"/></svg></div>
    <div class="step rule abs" style="top:94px"><span>Design</span>
      <svg width="16" height="16" viewBox="0 0 16 16"><path d="M8 1v14M1 8h14" stroke="#fff" stroke-width="1.3"/></svg></div>
    <div class="step abs" style="top:159px"><span>Realisation</span>
      <svg width="16" height="16" viewBox="0 0 16 16"><path d="M8 1v14M1 8h14" stroke="#fff" stroke-width="1.3"/></svg></div>
  </section>

  <section class="projects abs" role="img" aria-label="Helles, verblasstes Foto eines Wohnraums mit Regal">
    <div class="projects-veil abs"></div>
    <h2 class="abs">Zu den Projekten</h2>
    <p class="abs">Lassen Sie sich inspirieren - eine Übersicht unserer Referenzen finden Sie hier:</p>
    <div class="projects-button abs">Referenzen</div>
  </section>

  <footer class="site-footer abs">
    <div class="footer-contact abs"><a href="#">lena@raumwerk-studio.ch</a> &nbsp;-&nbsp; 079 512 44 80 &nbsp;-&nbsp; Lindenweg 7, 6020 Emmenbrücke</div>
    <div class="footer-links abs"><a href="#">Impressum</a><a href="#">Datenschutz</a><a href="#">Cookie-Einstellungen</a></div>
  </footer>

  <div class="builder-note abs"><span class="builder-name">Nuvelio</span><span>Das kannst du auch! Melde dich kostenlos an bei <a href="#">https://nuvelio.example/</a></span></div>
</body>
</html>
```